Help us share the power of history

We need 5 flyers (they can be similar in design, just small content changes in the front) and 1 large poster.

Paper Lantern? is a movement that aims to change the history market so that everyone gets what they need to be a changemaker of society. We've been selected as one of the most promising startups in Massachusetts and we will have a booth at Brightforge's Pitch Day.

We are trying to attract the attention of people walking buy to invest in our kickstarter campaign.

Target Market(s)

500-1,000 social entrepreneurs who are going to be walking around a large convention hall - so everything in terms of colors and design needs to be attractive

Industry/Entity Type

Non Profit

Font styles to use
Other font styles liked:
• Phoenix American

Colors

Designer to choose colors to be used in the design.

Requirements
Must have
• Font type: Phoenix American
• Modern
• Easy to read
• Eye-catching
• Please see attached document for more information.

```html
<!DOCTYPE html>
<html lang="en">
<head>
<meta charset="utf-8">
<title>Paper Lantern? – Vitamin Flyers</title>
<link rel="stylesheet" href="https://fonts.googleapis.com/css2?family=Antonio:wght@300;400&family=Mulish:wght@400;700&display=swap">
<style>
  :root {
    --canvas: #707070;
    --white: #ffffff;
    --orange: #ff7200;
    --green: #00e020;
    --red: #e01008;
    --yellow: #e8bc00;
    --purple: #a800e8;
    --display: "Antonio", "Arial Narrow", sans-serif;
    --body: "Mulish", "Century Gothic", sans-serif;
  }
  * { box-sizing: border-box; margin: 0; padding: 0; }
  html, body {
    width: 1200px; height: 2635px; overflow: hidden;
    background: var(--canvas);
  }
  .sheet { position: relative; width: 1200px; height: 2635px; }
  .flyer-pair { position: absolute; left: 100px; top: var(--top); width: 993px; height: 446px; }
  .flyer {
    position: absolute; top: 0; width: 448px; height: 446px;
    border-radius: 54px;
    background: var(--tone);
    box-shadow: 4px 6px 10px rgba(0,0,0,0.45);
  }
  .flyer--front { left: 0; }
  .flyer--back { left: 545px; }

  .title-panel {
    position: absolute; left: 26px; top: 33px; width: 396px; height: 276px;
    background: var(--white); border-radius: 44px;
    box-shadow: inset 0 0 0 1px rgba(0,0,0,0.15);
  }
  .title-panel svg { display: block; width: 100%; height: 100%; }
  .title-word {
    font-family: var(--display); font-weight: 400;
    font-size: 118px; fill: var(--tone);
  }
  .tagline {
    position: absolute; left: 0; right: 0; top: 340px;
    text-align: center; color: var(--white);
    font-family: var(--body); font-weight: 700; font-size: 27px;
  }
  .tagline--small { font-size: 23px; top: 343px; }

  .pitch-panel {
    position: absolute; left: 28px; top: 40px; width: 392px; height: 153px;
    background: var(--white); border-radius: 40px;
    box-shadow: inset 0 0 0 1px rgba(0,0,0,0.15);
    display: flex; align-items: center; justify-content: center;
    text-align: center; color: var(--tone);
    font-family: var(--body); font-weight: 400; font-size: 25px; line-height: 32px;
  }
  .site-address { position: absolute; left: 0; top: 252px; width: 448px; height: 70px; }
  .site-address svg { display: block; width: 100%; height: 100%; }
  .site-address text {
    font-family: var(--display); font-weight: 300; font-size: 54px; fill: var(--white);
  }

  .tone-orange { --tone: var(--orange); }
  .tone-green  { --tone: var(--green); }
  .tone-red    { --tone: var(--red); }
  .tone-yellow { --tone: var(--yellow); }
  .tone-purple { --tone: var(--purple); }
</style>
</head>
<body>
<main class="sheet">

  <section class="flyer-pair tone-orange" style="--top:67px">
    <article class="flyer flyer--front">
      <div class="title-panel">
        <svg viewBox="0 0 396 276" aria-label="Vitamin Community">
          <text class="title-word" x="198" y="119" text-anchor="middle" textLength="252" lengthAdjust="spacingAndGlyphs">VITAMIN</text>
          <text class="title-word" x="198" y="234" text-anchor="middle" textLength="369" lengthAdjust="spacingAndGlyphs">COMMUNITY</text>
        </svg>
      </div>
      <p class="tagline">You belong here.</p>
    </article>
    <article class="flyer flyer--back">
      <p class="pitch-panel">Support our movement<br>and help us build Boston’s<br>first AR map</p>
      <div class="site-address"><svg viewBox="0 0 448 70"><text x="224" y="55" text-anchor="middle" textLength="353" lengthAdjust="spacingAndGlyphs">WWW.PAPER-LANTERN.ORG</text></svg></div>
    </article>
  </section>

  <section class="flyer-pair tone-green" style="--top:580px">
    <article class="flyer flyer--front">
      <div class="title-panel">
        <svg viewBox="0 0 396 276" aria-label="Vitamin Agency">
          <text class="title-word" x="198" y="119" text-anchor="middle" textLength="293" lengthAdjust="spacingAndGlyphs">VITAMIN</text>
          <text class="title-word" x="198" y="234" text-anchor="middle" textLength="279" lengthAdjust="spacingAndGlyphs">AGENCY</text>
        </svg>
      </div>
      <p class="tagline">You have power.</p>
    </article>
    <article class="flyer flyer--back">
      <p class="pitch-panel">Support our movement<br>and help us build Boston’s<br>first AR map</p>
      <div class="site-address"><svg viewBox="0 0 448 70"><text x="224" y="55" text-anchor="middle" textLength="353" lengthAdjust="spacingAndGlyphs">WWW.PAPER-LANTERN.ORG</text></svg></div>
    </article>
  </section>

  <section class="flyer-pair tone-red" style="--top:1100px">
    <article class="flyer flyer--front">
      <div class="title-panel">
        <svg viewBox="0 0 396 276" aria-label="Vitamin Empathy">
          <text class="title-word" x="198" y="119" text-anchor="middle" textLength="275" lengthAdjust="spacingAndGlyphs">VITAMIN</text>
          <text class="title-word" x="198" y="234" text-anchor="middle" textLength="300" lengthAdjust="spacingAndGlyphs">EMPATHY</text>
        </svg>
      </div>
      <p class="tagline">We all matter.</p>
    </article>
    <article class="flyer flyer--back">
      <p class="pitch-panel">Support our movement<br>and help us build Boston’s<br>first AR map</p>
      <div class="site-address"><svg viewBox="0 0 448 70"><text x="224" y="55" text-anchor="middle" textLength="353" lengthAdjust="spacingAndGlyphs">WWW.PAPER-LANTERN.ORG</text></svg></div>
    </article>
  </section>

  <section class="flyer-pair tone-yellow" style="--top:1608px">
    <article class="flyer flyer--front">
      <div class="title-panel">
        <svg viewBox="0 0 396 276" aria-label="Vitamin Imagination">
          <text class="title-word" x="198" y="119" text-anchor="middle" textLength="252" lengthAdjust="spacingAndGlyphs">VITAMIN</text>
          <text class="title-word" x="198" y="234" text-anchor="middle" textLength="372" lengthAdjust="spacingAndGlyphs">IMAGINATION</text>
        </svg>
      </div>
      <p class="tagline">Dare to dream.</p>
    </article>
    <article class="flyer flyer--back">
      <p class="pitch-panel">Support our movement<br>and help us build Boston’s<br>first AR map</p>
      <div class="site-address"><svg viewBox="0 0 448 70"><text x="224" y="55" text-anchor="middle" textLength="353" lengthAdjust="spacingAndGlyphs">WWW.PAPER-LANTERN.ORG</text></svg></div>
    </article>
  </section>

  <section class="flyer-pair tone-purple" style="--top:2108px">
    <article class="flyer flyer--front">
      <div class="title-panel">
        <svg viewBox="0 0 396 276" aria-label="Vitamin Context">
          <text class="title-word" x="198" y="119" text-anchor="middle" textLength="265" lengthAdjust="spacingAndGlyphs">VITAMIN</text>
          <text class="title-word" x="198" y="234" text-anchor="middle" textLength="276" lengthAdjust="spacingAndGlyphs">CONTEXT</text>
        </svg>
      </div>
      <p class="tagline tagline--small">You understand the full picture.</p>
    </article>
    <article class="flyer flyer--back">
      <p class="pitch-panel">Support our movement<br>and help us build Boston’s<br>first AR map</p>
      <div class="site-address"><svg viewBox="0 0 448 70"><text x="224" y="55" text-anchor="middle" textLength="353" lengthAdjust="spacingAndGlyphs">WWW.PAPER-LANTERN.ORG</text></svg></div>
    </article>
  </section>

</main>
</body>
</html>
```